We need a very creative business card for a leading diamond tools manufactures in india

1. Iso 9001:2000
2. Logo
3. Leading Manufacture of stone cutting tools: Gang Saw Segment, Circular Segment, wire saw segment and rubber and plastic coated diamond wire rope.
4. Spirit for success
5. Kalvani Mokesh Diamond Tools Pvt. Ltd.
6. Mo. No. 9817406352
7. Email: Rakesh@kmgroup-tardex.com
8. Web: kmgroup-tardex.com
9.CEO
10. Reg. Office. 47, pushpa vihar , naya basti, dholpura ,dist. Rajsamand (rajasthan) 313587
11.Rakesh Jandal
Our audience are Adult based in english speaking person having age between 25-55 that handle granite and marble business.
Plastic

```html
<!DOCTYPE html>
<html lang="en">
<head>
<meta charset="UTF-8">
<title>KMG Business Card</title>
<link rel="stylesheet" href="https://fonts.googleapis.com/css2?family=Montserrat:wght@400;500;700&family=Oswald:wght@500;600&display=swap">
<style>
  :root {
    --bg: #e8e5e0;
    --card: #ffffff;
    --orange: #f5a01a;
    --orange-deep: #ef9412;
    --yellow: #f8d21c;
    --ink: #3b2c12;
    --ink-soft: #5a4a30;
    --icon: #e0502a;
  }
  * { margin: 0; padding: 0; box-sizing: border-box; }
  html, body { width: 1200px; height: 905px; overflow: hidden; }
  body {
    background: var(--bg);
    position: relative;
    font-family: "Montserrat", sans-serif;
  }
  .card {
    position: absolute;
    width: 620px;
    height: 354px;
    background: var(--card);
    box-shadow: 0 10px 26px rgba(60, 45, 20, 0.18);
    overflow: hidden;
  }
  .card--front { left: 60px; top: 70px; }
  .card--back { left: 520px; top: 480px; }
  .card__shapes { position: absolute; inset: 0; width: 100%; height: 100%; }

  .brand {
    position: absolute;
    display: flex;
    align-items: center;
    gap: 10px;
  }
  .brand__dot {
    width: 22px; height: 22px;
    border-radius: 50%;
    background: var(--orange);
  }
  .brand__name {
    font-family: "Montserrat", sans-serif;
    font-weight: 700;
    font-size: 34px;
    color: var(--orange);
    letter-spacing: 1px;
  }
  .card--front .brand { right: 40px; top: 44px; }
  .card--back .brand { left: 40px; top: 44px; }

  .front__web {
    position: absolute;
    left: 40px; top: 207px;
    font-size: 13px;
    font-weight: 500;
    letter-spacing: 3px;
    color: #fff;
  }

  .back__address {
    position: absolute;
    left: 40px; top: 186px;
    font-size: 13px;
    font-weight: 500;
    color: #fff;
  }
  .back__person {
    position: absolute;
    left: 430px; top: 152px;
    color: var(--ink);
  }
  .back__name {
    font-family: "Oswald", sans-serif;
    font-weight: 600;
    font-size: 26px;
    letter-spacing: 1px;
    line-height: 1;
  }
  .back__role {
    font-size: 10px;
    font-weight: 700;
    letter-spacing: 1.5px;
    margin-top: 4px;
  }
  .contacts {
    position: absolute;
    left: 40px; top: 240px;
    list-style: none;
  }
  .contacts li {
    display: flex;
    align-items: center;
    gap: 8px;
    font-size: 11px;
    color: var(--ink-soft);
    height: 19px;
  }
  .contacts svg { width: 10px; height: 10px; fill: var(--icon); }
</style>
</head>
<body>

<section class="card card--front">
  <svg class="card__shapes" viewBox="0 0 620 354" aria-hidden="true">
    <polygon points="0,190 432,190 392,244 0,244" fill="var(--orange)"/>
  </svg>
  <div class="brand">
    <span class="brand__dot"></span>
    <span class="brand__name">KMG</span>
  </div>
  <p class="front__web">www.kmgtoolsite.com</p>
</section>

<section class="card card--back">
  <svg class="card__shapes" viewBox="0 0 620 354" aria-hidden="true">
    <rect x="0" y="172" width="620" height="46" fill="var(--orange)"/>
    <polygon points="425,118 600,118 600,250 375,250" fill="var(--yellow)"/>
    <polygon points="588,108 620,108 620,228 600,250 588,250" fill="var(--orange-deep)"/>
  </svg>
  <div class="brand">
    <span class="brand__dot"></span>
    <span class="brand__name">KMG</span>
  </div>
  <p class="back__address">72,MK,Lane Road, 5th block Street n.</p>
  <div class="back__person">
    <p class="back__name">MIRA KESTON</p>
    <p class="back__role">GENERAL MANAGER</p>
  </div>
  <ul class="contacts">
    <li>
      <svg viewBox="0 0 10 10"><path d="M2 0.5l2 2-1 1.2c.6 1.3 1.6 2.3 2.9 2.9l1.2-1 2 2-1.3 1.6C4.5 9 1 5.5.6 1.8z"/></svg>
      031 628 4057
    </li>
    <li>
      <svg viewBox="0 0 10 10"><path d="M2.5 0h5v10h-5zM3.5 1v7h3V1z"/></svg>
      031 628 4057
    </li>
    <li>
      <svg viewBox="0 0 10 10"><path d="M0 2h10v6H0zM1 3v.4l4 2.4 4-2.4V3z"/></svg>
      hello@kmgmail.com
    </li>
    <li>
      <svg viewBox="0 0 10 10"><circle cx="5" cy="5" r="5"/></svg>
      www.kmgtoolsite.com
    </li>
  </ul>
</section>

</body>
</html>
```